Vantix 220 for Slate

We are looking to design a page for the mobile app. The app is intended for financial professionals and is based on a successful desktop application. The existing design will serve as a very rough guideline, but we are open to hearing ideas.
Uploaded file #1 contains a screenshot of the existing design. The workflow is as follows:
The user picks a portfolio from the Dropdown below portfolio.
The user picks a Loss Threshold, which will dictate what gets onto the bubble chart below.
Once the bubble on the chart is clicked, a text box pops up with the description of the particular crisis that the bubble represents.
Once the bubble is clicked, the right hand side bar charts are populated with moves relevant to this scenario.
The left hand pane contains two text boxes. The lower one is particularly important, because the user is able to remove scenarios or add scenarios (screen #2). Removing scenarios is simple.
Adding scenarios brings up a wizard (screen #3). It also needs to be designed consistently with the front page of the app. The wizard has different clickable categories going down the column on the left and in a row on the top. The user can pick some or all of these categories.

Notes: The app should be designed for landscape mode only. The key to keep in mind is how the user will select bubbles on the chart. Right now, it is quite easy, but with the touchscreen it may be more complicated, so please keep that in mind when designing the chart (it should still be some version of the similar chart).
*As a first pass, please submit your idea of the concept (layout/colors/buttons) without the detailed design. We will choose 1-3 concepts and then the detailed work will take place with a much higher chance of a payout.
Updates

Thank you for the first two sketches. The second one by bertrand appears to be a bit more mobile app oriented, though we are still considering both and waiting for other submissions. One request, could you rework the sketches to include a bit more of dark blue as a background?  \

Bertrand, I think that the bubbles are too small and they are missing some volume effects. Could you make them a bit more prominent (and pick some form of dark blue background) and change the color to see if they will stand out better?
 

Industry/Entity Type

Financial

Requirements
Must have
• The general outline for the bubble chart must be retained. But the actual execution may differ significantly. We are open to seeing different ideas.
The winning design will also get a contract to design the rest of the application (2 more screens), which will be worth the same as the original design.

```html
<!DOCTYPE html>
<html lang="en">
<head>
<meta charset="utf-8">
<title>Vantix 220 — Scenario Dashboard</title>
<link rel="stylesheet" href="https://fonts.googleapis.com/css2?family=Source+Sans+3:wght@400;600&display=swap">
<style>
:root{
  --page:#1d1e22;
  --screen:#1d1e22;
  --bar-black:#050506;
  --panel:#141518;
  --panel-head:#0d0e10;
  --btn-top:#3d3e42;
  --btn-bot:#2a2b2e;
  --btn-edge:#4b4c50;
  --text:#f1f2f4;
  --muted:#a7a9ae;
  --row-hi-a:#3a9bb8;
  --row-hi-b:#1f5d73;
  --green:#6fc12d;
  --orange:#e8621f;
  --track:#2a2b2f;
}
*{box-sizing:border-box;margin:0;padding:0}
html,body{width:1200px;height:957px;overflow:hidden;background:var(--page)}
body{font-family:"Source Sans 3",sans-serif;color:var(--text)}
.screen{position:absolute;left:0;top:28px;width:904px;height:678px;transform:scale(1.3274);transform-origin:0 0;background:var(--screen);overflow:hidden}
.abs{position:absolute}
.status{left:0;top:0;width:904px;height:20px;background:var(--bar-black);font-size:10px;font-weight:600;display:flex;align-items:center;justify-content:space-between;padding:0 8px}
.status .time{position:absolute;left:0;right:0;text-align:center}
.status .battery{display:flex;align-items:center;gap:3px}
.toolbar-item{top:22px;height:50px;display:flex}
.toolbar-item .field{flex:1;background:linear-gradient(var(--btn-top),var(--btn-bot));border:1px solid var(--btn-edge);border-right:none;border-radius:3px 0 0 3px;text-align:center;padding-top:9px;white-space:nowrap;overflow:hidden}
.toolbar-item .value{font-size:12.5px;font-weight:600;line-height:14px}
.toolbar-item .label{font-size:9.5px;color:var(--muted);line-height:12px}
.toolbar-item .drop{width:24px;background:linear-gradient(#55565a,#3a3b3e);border:1px solid var(--btn-edge);border-radius:0 3px 3px 0;display:flex;align-items:center;justify-content:center;color:#9a9ca0;font-size:8px}
.stepper{width:24px;display:flex;flex-direction:column;border:1px solid var(--btn-edge);border-radius:0 3px 3px 0;overflow:hidden}
.stepper span{flex:1;background:linear-gradient(#55565a,#3a3b3e);display:flex;align-items:center;justify-content:center;color:#cfd0d3;font-size:13px}
.stepper span+span{border-top:1px solid #2a2b2e}
.go{top:22px;left:857px;width:38px;height:50px;background:linear-gradient(#4a4b4f,#333438);border:1px solid var(--btn-edge);border-radius:3px;display:flex;align-items:center;justify-content:center;color:#9fa1a5;font-size:12px}
.checks{top:78px;left:12px;font-size:9.5px;color:var(--muted);display:flex;gap:26px}
.checks span{display:flex;align-items:center;gap:7px}
.panel{background:var(--panel)}
.panel-title{height:30px;background:var(--panel-head);font-size:18px;font-weight:600;padding:3px 9px;position:relative;white-space:nowrap}
.star{position:absolute;right:0;top:0;width:27px;height:30px;background:linear-gradient(#5a5b5f,#3c3d41);display:flex;align-items:center;justify-content:center}
.cols,.row{display:grid;grid-template-columns:114px 104px 1fr;padding-left:10px;white-space:nowrap}
.cols{font-size:9px;height:22px;align-items:center;margin-top:4px}
.row{height:27.6px;align-items:center;font-size:12px}
.row span{overflow:hidden}
.row.selected{background:linear-gradient(90deg,var(--row-hi-a),var(--row-hi-b))}
.row .shock{padding-left:6px}
.asset-row{height:27px;position:relative;font-size:11px;white-space:nowrap}
.asset-row.tight{height:23px}
.asset-row .name{position:absolute;left:4px;top:2px}
.asset-row .val{position:absolute;right:8px;top:2px}
.asset-row .track{position:absolute;left:4px;right:8px;bottom:6px;height:3px;background:var(--track)}
.asset-row .fill{position:absolute;top:0;height:3px;border-radius:2px}
.highest .fill{left:0;background:var(--green)}
.lowest .fill{right:0;background:var(--orange)}
.scroll{right:4px;top:44px;width:3px;height:122px;background:#cfd0d3;border-radius:2px}
</style>
</head>
<body>
<main class="screen">
  <header class="abs status">
    <span>Slate
      <svg width="12" height="9" viewBox="0 0 12 9"><path d="M1 3.5a7 7 0 0 1 10 0M3 5.5a4 4 0 0 1 6 0" stroke="#fff" stroke-width="1.4" fill="none"/><circle cx="6" cy="7.6" r="1.1" fill="#fff"/></svg>
    </span>
    <span class="time">3:14 PM</span>
    <span class="battery">32 %
      <svg width="18" height="9" viewBox="0 0 18 9"><rect x=".5" y=".5" width="15" height="8" rx="1.5" stroke="#fff" fill="none"/><rect x="2" y="2" width="4" height="5" fill="#fff"/><rect x="16" y="3" width="1.5" height="3" fill="#fff"/></svg>
    </span>
  </header>

  <div class="abs toolbar-item" style="left:8px;width:114px"><div class="field"><div class="value">14 Jul 2013</div><div class="label">Portfolio Date</div></div><div class="drop">▼</div></div>
  <div class="abs toolbar-item" style="left:127px;width:113px"><div class="field"><div class="value">QVX BB</div><div class="label">Portfolio</div></div><div class="drop">▼</div></div>
  <div class="abs toolbar-item" style="left:245px;width:97px"><div class="field"><div class="value">USD</div><div class="label">Currency</div></div><div class="drop">▼</div></div>
  <div class="abs toolbar-item" style="left:345px;width:155px"><div class="field"><div class="value">6 Dec 2012</div><div class="label">Model Date &nbsp;|&nbsp; Real Model</div></div><div class="drop">▼</div></div>
  <div class="abs toolbar-item" style="left:505px;width:113px"><div class="field"><div class="value">Active</div><div class="label">Weight type</div></div><div class="drop">▼</div></div>
  <div class="abs toolbar-item" style="left:622px;width:114px"><div class="field"><div class="value">Qorvane</div><div class="label">Model</div></div><div class="drop">▼</div></div>
  <div class="abs toolbar-item" style="left:740px;width:113px"><div class="field"><div class="value">-10</div><div class="label">Loss Threshold</div></div><div class="stepper"><span>+</span><span>–</span></div></div>
  <div class="abs go">Go</div>

  <div class="abs checks">
    <span><svg width="11" height="9" viewBox="0 0 11 9"><path d="M1 4.5l3 3 6-6.5" stroke="#6fc12d" stroke-width="2" fill="none"/></svg>Only Key Scenarios</span>
    <span><svg width="11" height="9" viewBox="0 0 11 9"><path d="M1 4.5l3 3 6-6.5" stroke="#9a9ca0" stroke-width="2" fill="none"/></svg>Other Secondry Optional Check Menu</span>
  </div>

  <section class="abs panel" style="left:8px;top:100px;width:280px;height:242px">
    <h2 class="panel-title">Shocks<span class="star"><svg width="11" height="11" viewBox="0 0 12 12"><path d="M6 .5l1.6 3.6 3.9.4-2.9 2.6.8 3.9L6 9 2.6 11l.8-3.9L.5 4.5l3.9-.4z" fill="#141518"/></svg></span></h2>
    <div class="cols"><span>Name</span><span>Type</span><span>Shock</span></div>
    <div class="row"><span>United States</span><span>Equity Index</span><span class="shock">-15</span></div>
    <div class="row"><span>Gold</span><span>Macro / Style</span><span class="shock">60</span></div>
    <div class="row"><span>3 Years US Govern...</span><span>Interest Rate</span><span class="shock">3</span></div>
    <div class="row selected"><span>United States</span><span>Equity Index</span><span class="shock">-15</span></div>
    <div class="row"><span>Gold</span><span>Macro / Style</span><span class="shock">60</span></div>
    <div class="row"><span>3 Years US Govern...</span><span>Interest Rate</span><span class="shock">3</span></div>
    <div class="row"><span>3 Years US Govern...</span><span>Interest Rate</span><span class="shock">3</span></div>
  </section>

  <section class="abs panel" style="left:8px;top:351px;width:280px;height:299px">
    <h2 class="panel-title">Current Scenario<span class="star"><svg width="11" height="11" viewBox="0 0 12 12"><path d="M6 .5l1.6 3.6 3.9.4-2.9 2.6.8 3.9L6 9 2.6 11l.8-3.9L.5 4.5l3.9-.4z" fill="#141518"/></svg></span></h2>
    <div class="cols"><span>Name</span><span>Type</span><span>Shock</span></div>
    <div class="row"><span>United States</span><span>Equity Index</span><span class="shock">-15</span></div>
    <div class="row"><span>Gold</span><span>Macro / Style</span><span class="shock">60</span></div>
    <div class="row"><span>3 Years US Govern...</span><span>Interest Rate</span><span class="shock">3</span></div>
    <div class="row selected"><span>United States</span><span>Equity Index</span><span class="shock">-15</span></div>
    <div class="row"><span>Gold</span><span>Macro / Style</span><span class="shock">60</span></div>
    <div class="row"><span>3 Years US Govern...</span><span>Interest Rate</span><span class="shock">3</span></div>
    <div class="row"><span>3 Years US Govern...</span><span>Interest Rate</span><span class="shock">3</span></div>
    <div class="row"><span>3 Years US Govern...</span><span>Interest Rate</span><span class="shock">3</span></div>
    <div class="row"><span>3 Years US Govern...</span><span>Interest Rate</span><span class="shock">3</span></div>
  </section>

  <svg class="abs bubble-chart" style="left:295px;top:100px" width="598" height="308" viewBox="295 100 598 308" font-family="Source Sans 3, sans-serif">
    <defs>
      <radialGradient id="bubble" cx="35%" cy="30%" r="75%">
        <stop offset="0" stop-color="#c4ec6a"/><stop offset=".55" stop-color="#6fc12d"/><stop offset="1" stop-color="#3f7d12"/>
      </radialGradient>
    </defs>
    <rect x="295" y="100" width="598" height="308" fill="#141518"/>
    <g stroke="#4a4b50" stroke-width=".8" stroke-dasharray="3 2">
      <line x1="339" y1="126" x2="890" y2="126"/><line x1="339" y1="149" x2="890" y2="149"/><line x1="339" y1="172" x2="890" y2="172"/><line x1="339" y1="195" x2="890" y2="195"/><line x1="339" y1="217" x2="890" y2="217"/><line x1="339" y1="240" x2="890" y2="240"/><line x1="339" y1="263" x2="890" y2="263"/><line x1="339" y1="286" x2="890" y2="286"/><line x1="339" y1="309" x2="890" y2="309"/><line x1="339" y1="332" x2="890" y2="332"/><line x1="339" y1="355" x2="890" y2="355"/>
      <line x1="374" y1="103" x2="374" y2="378"/><line x1="409" y1="103" x2="409" y2="378"/><line x1="444" y1="103" x2="444" y2="378"/><line x1="479" y1="103" x2="479" y2="378"/><line x1="514" y1="103" x2="514" y2="378"/><line x1="548" y1="103" x2="548" y2="378"/><line x1="583" y1="103" x2="583" y2="378"/><line x1="618" y1="103" x2="618" y2="378"/><line x1="653" y1="103" x2="653" y2="378"/><line x1="688" y1="103" x2="688" y2="378"/><line x1="723" y1="103" x2="723" y2="378"/><line x1="758" y1="103" x2="758" y2="378"/><line x1="793" y1="103" x2="793" y2="378"/><line x1="828" y1="103" x2="828" y2="378"/><line x1="862" y1="103" x2="862" y2="378"/>
    </g>
    <line x1="339" y1="103" x2="339" y2="380" stroke="#d6d7da"/>
    <line x1="337" y1="378" x2="893" y2="378" stroke="#d6d7da"/>
    <g fill="#8e9095" font-size="8.5" text-anchor="end">
      <text x="333" y="106">-12</text><text x="333" y="129">-13</text><text x="333" y="152">-14</text><text x="333" y="175">-15</text><text x="333" y="198">-16</text><text x="333" y="220">-17</text><text x="333" y="243">-18</text><text x="333" y="266">-19</text><text x="333" y="289">-20</text><text x="333" y="312">-21</text><text x="333" y="335">-22</text><text x="333" y="358">-23</text><text x="333" y="381">-24</text>
    </g>
    <g fill="#8e9095" font-size="8.5" text-anchor="middle">
      <text x="339" y="395">-24</text><text x="374" y="395">-23</text><text x="409" y="395">-22</text><text x="444" y="395">-21</text><text x="479" y="395">-20</text><text x="514" y="395">-19</text><text x="548" y="395">-18</text><text x="583" y="395">-17</text><text x="618" y="395">-16</text><text x="653" y="395">-15</text><text x="688" y="395">-14</text><text x="723" y="395">-13</text><text x="758" y="395">-12</text><text x="793" y="395">-11</text><text x="828" y="395">-10</text><text x="862" y="395">-9</text>
      <text x="618" y="405" font-size="8">Loss</text>
    </g>
    <text x="311" y="240" fill="#8e9095" font-size="8" text-anchor="middle" transform="rotate(-90 311 240)">Correlation Surprise</text>
    <g text-anchor="middle" fill="#fff" font-weight="600">
      <circle cx="379" cy="139" r="6.5" fill="url(#bubble)"/><text x="379" y="142" font-size="8">3</text>
      <circle cx="836" cy="147" r="6.5" fill="url(#bubble)"/><text x="836" y="150" font-size="8">3</text>
      <circle cx="426" cy="322" r="6.5" fill="url(#bubble)"/><text x="426" y="325" font-size="8">3</text>
      <circle cx="729" cy="324" r="6.5" fill="url(#bubble)"/><text x="729" y="327" font-size="8">3</text>
      <circle cx="524" cy="270" r="9" fill="url(#bubble)" stroke="#2b5a0c" stroke-width="1"/><text x="524" y="274" font-size="10">3</text>
    </g>
    <g class="tooltip">
      <path d="M513 188h126a3 3 0 0 1 3 3v57a3 3 0 0 1-3 3h-97l-6 6-6-6h-17a3 3 0 0 1-3-3v-57a3 3 0 0 1 3-3z" fill="#1b1c20" stroke="#8e9095" stroke-width=".8"/>
      <g fill="#a7a9ae" font-size="8.5">
        <text x="517" y="202">Name: Stagflation Severe</text>
        <text x="517" y="220">Loss: -18.82</text>
        <text x="517" y="231">Plausibility: 0.00</text>
        <text x="517" y="242">Correlation Surprise: -18.82</text>
      </g>
    </g>
  </svg>

  <section class="abs panel highest" style="left:295px;top:412px;width:280px;height:238px">
    <h2 class="panel-title">Asset Contribution Highest<span class="star"><svg width="11" height="11" viewBox="0 0 12 12"><path d="M6 .5l1.6 3.6 3.9.4-2.9 2.6.8 3.9L6 9 2.6 11l.8-3.9L.5 4.5l3.9-.4z" fill="#141518"/></svg></span></h2>
    <div style="padding-top:2px">
      <div class="asset-row"><span class="name">KVRQ 6.505 02/12//67</span><span class="val">0.083</span><span class="track"><span class="fill" style="width:230px"></span></span></div>
      <div class="asset-row"><span class="name">PLDX G 6.505 02/12//67</span><span class="val">0.083</span><span class="track"><span class="fill" style="width:195px"></span></span></div>
      <div class="asset-row"><span class="name">Arlowe.505 02/12//67</span><span class="val">0.083</span><span class="track"><span class="fill" style="width:170px"></span></span></div>
      <div class="asset-row"><span class="name">QENZ 6.505 02/12//67</span><span class="val">0.083</span><span class="track"><span class="fill" style="width:148px"></span></span></div>
      <div class="asset-row tight"><span class="name">TORVIA S .505 02/12//67</span><span class="val">0.083</span><span class="track"><span class="fill" style="width:127px"></span></span></div>
      <div class="asset-row"><span class="name">ZNQ02/12//67</span><span class="val">0.003</span><span class="track"><span class="fill" style="width:78px"></span></span></div>
      <div class="asset-row tight"><span class="name">VELMQ 02/12//67</span><span class="val">0.002</span><span class="track"><span class="fill" style="width:45px"></span></span></div>
      <div class="asset-row tight"><span class="name">RQBXT 7.875 01/15/19</span><span class="val">0.001</span><span class="track"><span class="fill" style="width:25px"></span></span></div>
    </div>
  </section>

  <section class="abs panel lowest" style="left:580px;top:412px;width:313px;height:238px">
    <h2 class="panel-title">Asset Contribution Lowest<span class="star"><svg width="11" height="11" viewBox="0 0 12 12"><path d="M6 .5l1.6 3.6 3.9.4-2.9 2.6.8 3.9L6 9 2.6 11l.8-3.9L.5 4.5l3.9-.4z" fill="#141518"/></svg></span></h2>
    <div style="padding-top:2px;padding-right:40px;position:relative">
      <div class="asset-row"><span class="name">KVRQ 6.505 02/12//67</span><span class="val">0.083</span><span class="track"><span class="fill" style="width:250px"></span></span></div>
      <div class="asset-row"><span class="name">PLDX G 6.505 02/12//67</span><span class="val">0.083</span><span class="track"><span class="fill" style="width:220px"></span></span></div>
      <div class="asset-row"><span class="name">Arlowe.505 02/12//67</span><span class="val">0.083</span><span class="track"><span class="fill" style="width:190px"></span></span></div>
      <div class="asset-row"><span class="name">QENZ 6.505 02/12//67</span><span class="val">0.083</span><span class="track"><span class="fill" style="width:160px"></span></span></div>
      <div class="asset-row tight"><span class="name">TORVIA S .505 02/12//67</span><span class="val">0.083</span><span class="track"><span class="fill" style="width:140px"></span></span></div>
      <div class="asset-row"><span class="name">ZNQ02/12//67</span><span class="val">0.003</span><span class="track"><span class="fill" style="width:60px"></span></span></div>
      <div class="asset-row tight"><span class="name">VELMQ 02/12//67</span><span class="val">0.002</span><span class="track"><span class="fill" style="width:42px"></span></span></div>
      <div class="asset-row tight"><span class="name">RQBXT 7.875 01/15/19</span><span class="val">0.001</span><span class="track"><span class="fill" style="width:28px"></span></span></div>
    </div>
    <span class="abs scroll"></span>
  </section>
</main>
</body>
</html>
```